New business card/stationary for a consulting company

I am looking for a clean and very professional looking business card for my consulting company as well as corresponding stationary. I am uploading our logo. I like simple and powerful for the feel. No graphics but I am open on everything else. Below is my contact information but would like the final to be in a version I can add my employees information into and print. Thank you.

Daniel Whitcombe
dan@fernlowadvisory.com
2837 North 9th Avenue, Summit Floor, Oak Brook, Illinois 60483
www.fernlowadvisory.com

Industry/Entity Type

Consulting

Contact Information for Business Card

Daniel Whitcombe
dan@fernlowadvisory.com
www.fernlowadvisory.com

Font styles to use
Serif
Sans Serif

Requirements
Must have
• Our logo and the business card details.
Nice to have
• our website www.fernlowadvisory.com

```html
<!DOCTYPE html>
<html lang="en">
<head>
<meta charset="utf-8">
<title>Fernlow Advisory – Business Card</title>
<link rel="stylesheet" href="https://fonts.googleapis.com/css2?family=Questrial&family=Arimo:wght@400;700&display=swap">
<style>
  :root {
    --navy: #0b0f63;
    --navy-deep: #05083d;
    --paper: #f3f3f3;
    --band-grey: #7c7c7c;
    --ink: #1c1c1c;
    --backdrop: #1b1b1b;
    --white: #ffffff;
  }
  * { margin: 0; padding: 0; box-sizing: border-box; }
  html, body {
    width: 1200px; height: 1001px; overflow: hidden;
    background: var(--backdrop);
  }
  .sheet { position: relative; width: 1200px; height: 1001px; }
  .card {
    position: absolute; left: 306px; width: 588px; height: 329px;
    text-align: center; overflow: hidden;
  }
  .card--front { top: 137px; background: var(--paper); }
  .card--back {
    top: 534px;
    background: linear-gradient(180deg, #0d1270 0%, var(--navy) 45%, var(--navy-deep) 100%);
  }
  .brand-mark {
    position: absolute; left: 50%; transform: translateX(-50%);
    background: var(--navy);
  }
  .card--front .brand-mark { top: 56px; width: 34px; height: 34px; }
  .card--back .brand-mark { top: 104px; width: 50px; height: 50px; background: var(--white); }
  .brand-name {
    position: absolute; left: 0; right: 0;
    font-family: "Questrial", sans-serif; letter-spacing: 0.04em;
    white-space: nowrap;
  }
  .card--front .brand-name { top: 104px; font-size: 22px; color: var(--navy); }
  .card--back .brand-name { top: 172px; font-size: 30px; color: var(--white); }
  .person-name {
    position: absolute; left: 0; right: 0; top: 187px;
    font-family: "Arimo", sans-serif; font-weight: 700; font-size: 19px;
    color: var(--navy); letter-spacing: 0.01em;
  }
  .contact {
    position: absolute; left: 0; right: 0; top: 256px;
    font-family: "Arimo", sans-serif; font-size: 13.5px; line-height: 16px;
    color: var(--ink);
  }
  .back-url {
    position: absolute; left: 0; right: 0; top: 277px;
    font-family: "Arimo", sans-serif; font-size: 13.5px; color: var(--white);
  }
  .footer-band { position: absolute; left: 0; bottom: 0; width: 588px; height: 16px; }
</style>
</head>
<body>
  <main class="sheet">
    <section class="card card--front" aria-label="Business card front">
      <div class="brand-mark"></div>
      <div class="brand-name">FERNLOW ADVISORY</div>
      <div class="person-name">DANIEL WHITCOMBE</div>
      <div class="contact">
        <p>dan@fernlowadvisory.com&nbsp; / &nbsp;www.fernlowadvisory.com</p>
        <p>2837 North 9th Avenue, Summit Floor, Oak Brook, Illinois 60483</p>
      </div>
      <svg class="footer-band" viewBox="0 0 588 16" aria-hidden="true">
        <polygon points="0,7 66,7 60,16 0,16" fill="var(--band-grey)"/>
        <polygon points="528,7 588,7 588,16 534,16" fill="var(--band-grey)"/>
        <polygon points="68,0 520,0 530,16 58,16" fill="var(--navy)"/>
      </svg>
    </section>

    <section class="card card--back" aria-label="Business card back">
      <div class="brand-mark"></div>
      <div class="brand-name">FERNLOW ADVISORY</div>
      <div class="back-url">www.fernlowadvisory.com</div>
    </section>
  </main>
</body>
</html>
```